Business Card for Brevel Coatings

We need a simple, yet out standing business card for our painting company.

Target Market(s)

wealthy; high-end neighborhoods, and businesses

Industry/Entity Type

Painting

Contact Information for Business Card

Name:
Doran Vask

Email:
d.vask@brevel-coatings.com

Website:
Brevel-coatings.com

Phone Number:
(555) 416-9073

Font styles to use
Serif
Sans Serif

Requirements
Must have
• slogan "making change simple"
Should not have
• A title attached to the name on the card

```html
<!DOCTYPE html>
<html lang="en">
<head>
<meta charset="utf-8">
<title>Brevel Coatings Business Card</title>
<link rel="stylesheet" href="https://fonts.googleapis.com/css2?family=Quattrocento:wght@400&display=swap">
<style>
  :root {
    --backdrop: #a3a1a2;
    --card-green: #41532f;
    --brand-lime: #8cc63f;
    --ink-light: #f2f2ec;
  }
  html, body {
    margin: 0;
    padding: 0;
    width: 1200px;
    height: 1200px;
    overflow: hidden;
    background: var(--backdrop);
  }
  .canvas {
    position: relative;
    width: 1200px;
    height: 1200px;
  }
  .card {
    position: absolute;
    background: var(--card-green);
    overflow: hidden;
  }
  .card--front { left: 238px; top: 117px; width: 713px; height: 420px; }
  .card--back  { left: 231px; top: 643px; width: 713px; height: 418px; }

  .brand {
    position: absolute;
    font-family: "Quattrocento", serif;
    font-weight: 400;
    white-space: nowrap;
  }
  .brand__name {
    margin: 0;
    font-weight: 400;
    letter-spacing: 1px;
    line-height: 1.1;
  }
  .brand__slogan {
    margin: 0;
    text-transform: uppercase;
    line-height: 1.2;
  }

  .card--front .brand {
    left: 0;
    right: 0;
    top: 176px;
    text-align: center;
    color: var(--brand-lime);
  }
  .card--front .brand__name { font-size: 56px; }
  .card--front .brand__slogan {
    margin-top: 8px;
    font-size: 20px;
    letter-spacing: 6px;
  }

  .card--back .brand {
    left: 44px;
    top: 186px;
    color: var(--ink-light);
  }
  .card--back .brand__name { font-size: 36px; }
  .card--back .brand__slogan {
    margin-top: 6px;
    font-size: 13px;
    letter-spacing: 3.4px;
  }

  .contact {
    position: absolute;
    left: 389px;
    top: 138px;
    font-family: "Quattrocento", serif;
    color: var(--ink-light);
  }
  .contact__name {
    margin: 0 0 24px 0;
    font-size: 31px;
    font-weight: 400;
    letter-spacing: 0.5px;
  }
  .contact__list {
    list-style: none;
    margin: 0;
    padding: 0;
  }
  .contact__item {
    display: flex;
    align-items: center;
    height: 29px;
    font-size: 19px;
    letter-spacing: 0.3px;
    white-space: nowrap;
  }
  .contact__icon {
    width: 18px;
    height: 18px;
    margin-right: 19px;
    flex: none;
    fill: var(--ink-light);
  }
</style>
</head>
<body>
<main class="canvas">
  <section class="card card--front" aria-label="Card front">
    <div class="brand">
      <h1 class="brand__name">Brevel Coatings</h1>
      <p class="brand__slogan">Making change simple</p>
    </div>
  </section>

  <section class="card card--back" aria-label="Card back">
    <div class="brand">
      <p class="brand__name">Brevel Coatings</p>
      <p class="brand__slogan">Making change simple</p>
    </div>
    <div class="contact">
      <h2 class="contact__name">Doran Vask</h2>
      <ul class="contact__list">
        <li class="contact__item">
          <svg class="contact__icon" viewBox="0 0 20 20" aria-hidden="true">
            <path d="M2 6c0-2 3-3 8-3s8 1 8 3v1.5h-4V6H6v1.5H2z"/>
            <path d="M5 9h10l2 8H3z"/>
          </svg>
          (555) 416-9073
        </li>
        <li class="contact__item">
          <svg class="contact__icon" viewBox="0 0 20 20" aria-hidden="true">
            <path d="M2 5h16v10H2z M3.5 6.2 10 11l6.5-4.8" fill="none" stroke="#f2f2ec" stroke-width="1.6"/>
          </svg>
          d.vask@brevel-coatings.com
        </li>
        <li class="contact__item">
          <svg class="contact__icon" viewBox="0 0 20 20" aria-hidden="true">
            <circle cx="10" cy="10" r="7.5" fill="none" stroke="#f2f2ec" stroke-width="1.5"/>
            <ellipse cx="10" cy="10" rx="3.2" ry="7.5" fill="none" stroke="#f2f2ec" stroke-width="1.3"/>
            <path d="M2.5 10h15M4 6h12M4 14h12" stroke="#f2f2ec" stroke-width="1.2"/>
          </svg>
          www.Brevel-coatings.com
        </li>
      </ul>
    </div>
  </section>
</main>
</body>
</html>
```